Corvale Holdings Business Cards

Hello. I need business cards designed with our new logo. I'd like to see at least 3 different designs. At least one with a dark background, and at least one with a white background. Maybe one with gray or blue for the background. Play with gradient colors and maybe even insert a pic of a skyline in the background of one or more of them. Use your judgement. We will need 2 cards printed. They need to accommodate the employee name, title, company address, phone, email, and website. Thanks.

Target Market(s)

Wealthy mature investors.

Contact Information for Business Card

Single-sided, professional, clean design that incorporates our logo.

Font styles to use
Sans Serif

Requirements
Must have
• Our new logo needs to be featured on it. (See attached.)
• Employee Name (In all CAPS)
• Title
• Street Address, City, ST Zip Code
• Cell Phone #, Email Address, Website Address
Nice to have
• Design that blends well with our new logo and its colors, or a city scape or other graphic design that looks like an apartment complex in the background. Blues and grays are nice, but use your judgement.
Should not have
• Modern or oriental looking designs or bright colors.

```html
<!DOCTYPE html>
<html lang="en">
<head>
<meta charset="utf-8">
<title>Corvale Holdings – Business Card</title>
<link href="https://fonts.googleapis.com/css2?family=Arimo:wght@400;700&display=swap" rel="stylesheet">
<style>
  :root {
    --night-deep: #07101c;
    --night-mid: #13223a;
    --night-glow: #2a3547;
    --accent-blue: #1e9be8;
    --text-white: #ffffff;
  }
  * { margin: 0; padding: 0; box-sizing: border-box; }
  html, body {
    width: 1200px;
    height: 601px;
    overflow: hidden;
    background: var(--night-deep);
  }
  .card {
    position: relative;
    width: 1200px;
    height: 601px;
    overflow: hidden;
    font-family: "Arimo", Arial, sans-serif;
    color: var(--text-white);
  }
  .skyline-backdrop {
    position: absolute;
    inset: 0;
    background:
      radial-gradient(ellipse 70% 45% at 50% 72%, var(--night-glow) 0%, rgba(42,53,71,0) 70%),
      linear-gradient(180deg, var(--night-deep) 0%, #0c1626 30%, var(--night-mid) 62%, #0d1829 100%);
  }
  .brand {
    position: absolute;
    left: 12px;
    top: 14px;
    display: flex;
    align-items: center;
    gap: 22px;
    color: var(--accent-blue);
    font-weight: 700;
  }
  .brand-square {
    width: 70px;
    height: 150px;
    background: var(--accent-blue);
  }
  .brand-name {
    line-height: 1;
  }
  .brand-name .primary {
    display: block;
    font-size: 84px;
    letter-spacing: 3px;
  }
  .brand-name .secondary {
    display: block;
    font-size: 40px;
    letter-spacing: 2px;
    margin-top: 8px;
  }
  .details {
    position: absolute;
    left: 0;
    right: 0;
    top: 214px;
    text-align: center;
  }
  .employee-name {
    font-size: 74px;
    font-weight: 700;
    letter-spacing: 4px;
    line-height: 1;
    margin-left: 10px;
  }
  .employee-name .surname { color: var(--accent-blue); }
  .employee-title {
    width: 862px;
    margin: 14px auto 0 165px;
    padding-bottom: 6px;
    border-bottom: 3px solid var(--text-white);
    font-size: 29px;
    font-weight: 700;
    letter-spacing: 1px;
  }
  .contact-list {
    list-style: none;
    margin-top: 8px;
    font-weight: 700;
    line-height: 1.2;
  }
  .contact-list .phone,
  .contact-list .email,
  .contact-list .website { font-size: 29px; letter-spacing: 1px; }
  .contact-list .address { font-size: 25px; letter-spacing: 1px; }
  .contact-list .phone { margin-left: 16px; }
  .contact-list .email { margin-left: 34px; }
  .contact-list .website { margin-left: 38px; }
</style>
</head>
<body>
  <main class="card">
    <div class="skyline-backdrop" role="img" aria-label="Night-time city skyline with illuminated skyscrapers and city lights"></div>

    <header class="brand">
      <span class="brand-square"></span>
      <span class="brand-name">
        <span class="primary">CORVALE</span>
        <span class="secondary">HOLDINGS, LLC</span>
      </span>
    </header>

    <section class="details">
      <h1 class="employee-name">DANIEL <span class="surname">MERCER</span></h1>
      <p class="employee-title">Principal (Manager) Brightmoor Legacy Partners, LLC</p>
      <ul class="contact-list">
        <li class="phone">(555) 014-2280</li>
        <li class="address">418 Linden Ct Ashby, Fairmont, 75000, Texas</li>
        <li class="email">youremail@email.com</li>
        <li class="website">www.website.com</li>
      </ul>
    </section>
  </main>
</body>
</html>
```